Spring Style Exclusive Shopping Party for women

We need a postcard design for our Spring Shopping Event. Willow Lane is a women's apparel and accessories store featuring missy, petite and plus sizes. Event is Saturday, April 1 from 9am-10am. Looking for a twist on the spring shopping party idea. Attaching 2 postcards we have previously sent for this event and 2 ideas for what we are looking for in new postcard.

Target Market(s)

women 20+

Industry/Entity Type

Retail

Font styles to use
Serif

Requirements
Must have
• must be eye catching, have the logo, date and time of event,
Nice to have
• woman model

```html
<!DOCTYPE html>
<html lang="en">
<head>
<meta charset="utf-8">
<title>Willow Lane – Spring Shopping Event Postcard</title>
<link rel="stylesheet" href="https://fonts.googleapis.com/css2?family=Cinzel:wght@400&family=Crimson+Pro:wght@500;600&family=Lato:wght@400;700&display=swap">
<style>
  :root {
    --page: #e8e8ea;
    --card: #ffffff;
    --sky-1: #f4f6f9;
    --sky-2: #e3e8ef;
    --red: #e2231a;
    --ink: #111111;
    --navy: #1f2f73;
    --band: #cfe3df;
    --rule: #8fa3d6;
    --text: #222222;
    --blue-text: #23408e;
    --line: #555555;
  }
  * { margin: 0; padding: 0; box-sizing: border-box; }
  html, body { width: 1200px; height: 1200px; overflow: hidden; background: var(--page); }
  body { position: relative; font-family: "Crimson Pro", serif; font-weight: 600; color: var(--ink); }

  .postcard {
    position: absolute; left: 230px; width: 752px; height: 496px;
    background: linear-gradient(135deg, var(--card) 0%, var(--sky-1) 45%, var(--sky-2) 100%);
    overflow: hidden;
  }
  .postcard--front { top: 32px; }
  .postcard--back { top: 654px; height: 502px; background: linear-gradient(160deg, var(--sky-1) 0%, var(--card) 55%, var(--sky-1) 100%); }
  .abs { position: absolute; white-space: nowrap; }

  .invite { left: 42px; top: 32px; font-family: "Cinzel", serif; font-size: 21px; color: var(--red); letter-spacing: 0.3px; }
  .brand-name { font-family: "Crimson Pro", serif; font-weight: 600; color: var(--ink); font-size: 52px; line-height: 1; }
  .front-brand { left: 66px; top: 100px; }
  .presents { left: 250px; top: 150px; font-size: 21px; }
  .event-band { left: 29px; top: 202px; width: 349px; height: 37px; background: var(--band); font-size: 28px; line-height: 37px; padding-left: 14px; }
  .discount { left: 88px; top: 264px; color: var(--red); line-height: 1; }
  .discount .pct { font-size: 64px; }
  .discount .off { font-size: 29px; margin-left: 22px; letter-spacing: 1px; }
  .entire { left: 58px; top: 332px; font-size: 39px; font-weight: 500; }
  .date { left: 82px; top: 394px; font-size: 27px; }
  .time { left: 88px; top: 426px; font-size: 30px; color: var(--navy); letter-spacing: 8px; }
  .photo { position: absolute; }
  .front-photo { left: 398px; top: 64px; width: 354px; height: 432px;
    background: radial-gradient(ellipse at 50% 70%, #f4ece2 0%, #ecd7c4 40%, #e7a184 70%, rgba(227,232,239,0) 100%); }
  .base-rule { position: absolute; left: 0; right: 0; height: 3px; background: var(--rule); }
  .postcard--front .base-rule { top: 488px; }

  .back-brand { left: 62px; top: 34px; font-size: 46px; }
  .back-event { left: 27px; top: 108px; font-size: 20px; }
  .row-label { left: 25px; font-size: 13px; color: var(--navy); letter-spacing: 0.5px; }
  .row-text { left: 81px; width: 232px; font-family: "Lato", sans-serif; font-weight: 400; font-size: 10.5px; line-height: 13px; white-space: normal; color: var(--text); text-align: justify; }
  .get-text { left: 81px; top: 210px; font-family: "Lato", sans-serif; font-weight: 400; font-size: 10.5px; color: var(--text); }
  .get-text b { color: var(--red); font-size: 16px; font-weight: 700; }
  .back-date { left: 48px; top: 252px; font-size: 24px; }
  .back-time { left: 50px; top: 279px; font-size: 19px; color: var(--navy); }
  .note { left: 27px; top: 320px; width: 190px; font-family: "Lato", sans-serif; font-weight: 400; font-size: 11px; line-height: 12.5px; white-space: normal; color: var(--text); }
  .note--blue { top: 358px; color: var(--blue-text); }
  .divider { position: absolute; left: 2px; width: 230px; height: 1px; background: #9a9a9a; }
  .contact { left: 27px; font-family: "Lato", sans-serif; font-weight: 400; font-size: 12px; color: var(--text); display: flex; align-items: center; gap: 6px; }
  .contact svg { width: 10px; height: 10px; }
  .back-photo { left: 262px; top: 240px; width: 180px; height: 250px;
    background: radial-gradient(ellipse at 50% 60%, #7fa6cf 0%, #2f4f87 45%, #1c2c55 65%, rgba(255,255,255,0) 100%); }
  .stamp-box { position: absolute; left: 611px; top: 37px; width: 86px; height: 88px; border: 1.5px solid var(--line); }
  .address-line { position: absolute; left: 426px; width: 256px; height: 1.5px; background: var(--line); }
  .postcard--back .base-rule { top: 494px; }
</style>
</head>
<body>

<section class="postcard postcard--front" aria-label="Postcard front">
  <div class="abs invite">YOU'RE INVITED</div>
  <div class="abs brand-name front-brand">Willow Lane</div>
  <div class="abs presents">Presents</div>
  <div class="abs event-band">Spring Shopping Event</div>
  <div class="abs discount"><span class="pct">30%</span><span class="off">OFF</span></div>
  <div class="abs entire">entire purchase</div>
  <div class="abs date">Saturday, April 1</div>
  <div class="abs time">9am-10am</div>
  <div class="photo front-photo" role="img" aria-label="Smiling woman in a white floral spring dress holding a mint handbag"></div>
  <div class="base-rule"></div>
</section>

<section class="postcard postcard--back" aria-label="Postcard back">
  <div class="abs brand-name back-brand">Willow Lane</div>
  <div class="abs back-event">Spring Shopping Event</div>

  <div class="abs row-label" style="top:141px">SHOP:</div>
  <div class="abs row-text" style="top:141px">Our limited-edition exclusives benefitting Suited Forward and selling out</div>
  <div class="abs row-label" style="top:176px">GIVE:</div>
  <div class="abs row-text" style="top:176px">Clean out yor closet! Tomorrow is the last day to bring in nearly new wear-to work</div>
  <div class="abs row-label" style="top:212px">GET:</div>
  <div class="abs get-text"><b>30% OFF</b> on entire purchase.</div>

  <div class="abs back-date">Saturday, April 1</div>
  <div class="abs back-time">9-10am in Maplebrook</div>

  <p class="abs note">Everyone will receive a gift bag plus great savings opportunities during this event.</p>
  <p class="abs note note--blue">Pastries and juice will be served to start your day off right!</p>

  <div class="divider" style="top:402px"></div>
  <div class="abs contact" style="top:407px">
    <svg viewBox="0 0 10 10" aria-hidden="true"><path d="M5 0.5a3.3 3.3 0 0 0-3.3 3.3C1.7 6.3 5 9.5 5 9.5s3.3-3.2 3.3-5.7A3.3 3.3 0 0 0 5 0.5z" fill="#1f2f73"/><circle cx="5" cy="3.8" r="1.2" fill="#fff"/></svg>
    Maplebrook,118 Orchard Ave</div>
  <div class="abs contact" style="top:423px">
    <svg viewBox="0 0 10 10" aria-hidden="true"><path d="M1 3.5c0-1.5 1.8-2.5 4-2.5s4 1 4 2.5H7V2.8H3v.7zM2 4.5h6l1 4.5H1z" fill="#1f2f73"/></svg>
    555-014-2200</div>
  <div class="abs contact" style="top:439px">
    <svg viewBox="0 0 10 10" aria-hidden="true"><rect x="0.7" y="1.5" width="8.6" height="6" fill="none" stroke="#1f2f73" stroke-width="1"/><path d="M3 9h4" stroke="#1f2f73"/></svg>
    www.willowlaneshop.com</div>
  <div class="divider" style="top:459px"></div>

  <div class="photo back-photo" role="img" aria-label="Blonde woman in a blue and white patterned dress, hand on hip"></div>

  <div class="stamp-box" aria-label="Stamp area"></div>
  <div class="address-line" style="top:230px"></div>
  <div class="address-line" style="top:253px"></div>
  <div class="address-line" style="top:276px"></div>
  <div class="base-rule"></div>
</section>

</body>
</html>
```